Real Estate Seller Financing Postcard

I need a postcard that lays out these options contained in the notes that grabs attention, explains the two options easily and is eye-catching. The front needs to have the percentages on it and information about it and on the other side One side exact Text is:
"Monthly income without tenant headaches" in big letters. Also on front "Get
110%
add an "or"
160% of market value for your property. ". The percentages should be displayed and that is not to be a sentence of text. Other side text: I need bullets points for these "Formal protection as a lien holder against home
No commission or closing cost
Fast closings possible
Property taken as is so no repairs.

Add to the top of the back in "It’s simple. I am a new investor without down payment capital who still want to double our portfolio this year to grow our portfolio."
Here are the two options that are to be the largest part of the back
Option 1, you can receive 80% now cash and 30% over a short period of time including interest.

Option 2, where act like a bank allowing you to make 150% if you finance the whole property(ies). No gimmicks and surprises, just simple unconventional financing.

Include Logo Somewhere

Target Market(s)

Property Owners Wanting to Sell Their Property

Industry/Entity Type

Real Estate Investing

Requirements
Must have
• The options promiment and each side with its respective information. Must have logo somewhere
Nice to have
• The options in color other than black.
Should not have
• A picture of money on the front. Any other image is okay.

```html
<!DOCTYPE html>
<html lang="en">
<head>
<meta charset="utf-8">
<title>Helios Property Group – Seller Financing Postcard</title>
<link rel="stylesheet" href="https://fonts.googleapis.com/css2?family=Montserrat:wght@400;500;600;700;800&family=Cookie&display=swap">
<style>
  :root{
    --blue:#0c3d96;
    --navy:#0f2a68;
    --grey-band:#7b8683;
    --ink:#222630;
    --white:#ffffff;
    --soft-white:#d9e3f7;
    --page:#e2e2e2;
  }
  *{box-sizing:border-box;margin:0;padding:0}
  html,body{width:712px;height:1200px;overflow:hidden;background:var(--page)}
  body{font-family:"Montserrat",Arial,sans-serif;position:relative}

  .postcard{position:absolute;left:46px;width:620px;height:387px;overflow:hidden;
    box-shadow:-4px 4px 8px rgba(0,0,0,.35);background:var(--white)}
  .postcard--front{top:170px}
  .postcard--back{top:630px}
  .postcard__inner{position:absolute;left:0;top:0;width:1157px;height:723px;
    transform:scale(.5359);transform-origin:0 0}
  .postcard__shapes{position:absolute;inset:0;width:1157px;height:723px}
  .abs{position:absolute;line-height:1}

  /* brand */
  .brand{display:flex;align-items:center;gap:22px}
  .brand__mark{width:90px;height:90px;border:4px solid var(--blue);border-radius:50%}
  .brand__name{color:var(--blue);font-weight:600}
  .brand__name span{display:block}
  .brand__name .l1{font-size:50px;letter-spacing:1px}
  .brand__name .l2{font-size:19px;margin-top:4px;letter-spacing:.5px}

  /* front */
  .headline{color:var(--white);font-weight:800}
  .headline .l1{display:block;font-size:86px;letter-spacing:1px}
  .headline .l2{display:block;font-size:99px;margin-top:-4px;letter-spacing:1px}
  .tagline{color:var(--white);font-size:37px;font-weight:500}
  .offer-label{color:var(--white);font-size:29px;font-weight:500}
  .offer-figure{color:var(--white);font-size:60px;font-weight:800}
  .offer-divider{background:var(--white);width:3px;height:86px}
  .offer-note{color:var(--white);font-size:26px;font-weight:500}
  .body-copy{color:var(--white);font-size:17px;line-height:1.2;width:480px}

  .contact{color:var(--ink);font-size:22px}
  .contact__title{font-weight:500;font-size:22px;letter-spacing:.5px}
  .contact__row{display:flex;align-items:center;gap:12px}
  .contact__row .hl{color:var(--blue)}
  .contact__phone{color:var(--blue);font-weight:700;font-size:31px}
  .icon{width:22px;height:22px;fill:var(--blue);flex:none}
  .contact--front{right:37px;text-align:right}
  .contact--front .contact__row{justify-content:flex-end}

  /* back */
  .script{font-family:"Cookie",cursive;color:var(--white);font-size:50px}
  .intro{color:var(--white);font-size:21px;line-height:1.17;width:470px}
  .benefits{left:37px;top:178px;width:484px;height:115px}
  .benefit{position:absolute;display:flex;gap:8px;color:var(--white);font-size:16px;font-weight:600;line-height:1.15}
  .benefit .icon{fill:var(--white);width:16px;height:16px;margin-top:1px}
  .benefits__v{position:absolute;left:250px;top:0;width:2px;height:115px;background:var(--white)}
  .benefits__h{position:absolute;left:0;top:62px;width:484px;height:2px;background:var(--white)}

  .option{color:var(--white);width:225px;font-size:17px;font-weight:500;line-height:1.25}
  .option__label{display:block;font-size:15px;font-weight:700;letter-spacing:2px;color:var(--soft-white);margin-bottom:6px}
  .option__figure{font-size:50px;font-weight:800;line-height:1;margin-right:8px}
  .option__big{display:block;margin:4px 0 6px}
  .option__inline{font-size:24px;font-weight:800}
  .options__divider{left:268px;top:305px;width:2px;height:168px;background:var(--white)}
  .option-tagline{color:var(--white);font-size:16px;font-weight:600;line-height:1.25;width:330px}

  .contact--back{left:37px}
  .contact--back .contact__row{font-size:17px}
  .contact--back .icon{width:18px;height:18px}
  .contact--back .contact__phone{font-size:20px}
  .stamp{border:2px solid var(--ink);width:145px;height:145px}
  .address-line{height:2px;width:432px;background:var(--ink)}
</style>
</head>
<body>

<!-- FRONT -->
<section class="postcard postcard--front" aria-label="Postcard front">
  <div class="postcard__inner">
    <svg class="postcard__shapes" viewBox="0 0 1157 723" aria-hidden="true">
      <defs>
        <linearGradient id="skyline" x1="0" y1="0" x2="0" y2="1">
          <stop offset="0" stop-color="#8fb4dc"/>
          <stop offset=".45" stop-color="#c8c3bb"/>
          <stop offset="1" stop-color="#9a6a4c"/>
        </linearGradient>
        <clipPath id="upperRight"><rect x="0" y="0" width="1157" height="520"/></clipPath>
      </defs>
      <rect width="1157" height="723" fill="var(--blue)"/>
      <g clip-path="url(#upperRight)">
        <circle cx="1040" cy="250" r="505" fill="var(--grey-band)"/>
        <circle cx="1040" cy="250" r="482" fill="url(#skyline)"/>
      </g>
      <path d="M700,723 C800,505 950,468 1157,462 L1157,723 Z" fill="var(--navy)"/>
      <path d="M580,723 C700,565 900,512 1157,516 L1157,723 Z" fill="var(--white)"/>
      <path d="M0,168 C230,200 420,130 492,0 L625,0 C500,190 260,230 0,212 Z" fill="var(--navy)"/>
      <path d="M0,0 L492,0 C420,130 230,200 0,178 Z" fill="var(--white)"/>
      <circle cx="662" cy="530" r="153" fill="#f1f1f1"/>
    </svg>
    <div class="abs" role="img" aria-label="Photo of modern high-rise towers under construction against a city skyline" style="left:560px;top:0;width:597px;height:460px"></div>
    <div class="abs" role="img" aria-label="Photo of a smiling real estate agent presenting a sketched city skyline"
         style="left:519px;top:387px;width:286px;height:286px;border-radius:50%;background:radial-gradient(circle at 45% 40%,#ffffff,#d4d6d8)"></div>

    <div class="abs brand" style="left:40px;top:38px">
      <div class="brand__mark"></div>
      <div class="brand__name"><span class="l1">HELIOS</span><span class="l2">PROPERTY GROUP</span></div>
    </div>

    <h1 class="abs headline" style="left:38px;top:222px"><span class="l1">MONTHLY</span><span class="l2">INCOME</span></h1>
    <p class="abs tagline" style="left:38px;top:395px">without tenant headaches</p>

    <p class="abs offer-label" style="left:38px;top:455px">Get</p>
    <p class="abs offer-label" style="left:235px;top:455px">add an "or"</p>
    <div class="abs offer-divider" style="left:202px;top:458px"></div>
    <p class="abs offer-figure" style="left:36px;top:497px">110%</p>
    <p class="abs offer-figure" style="left:233px;top:497px">160%</p>
    <p class="abs offer-note" style="left:38px;top:557px">of market value for your property.</p>
    <p class="abs body-copy" style="left:37px;top:604px">Lorem ipsum dolor sit amet, consectetur adipiscing elit, sed do eiusmod tempor incididunt ut labore et dolore magna aliqua. Ut enim ad minim veniam, quis nostrud exercitation ullamco laboris</p>

    <div class="abs contact contact--front" style="top:548px">
      <p class="contact__title">CONTACT INFORMATION</p>
      <p class="contact__row contact__phone" style="margin-top:20px"><span>5550142876</span>
        <svg class="icon" viewBox="0 0 24 24"><path d="M6.6 10.8a15 15 0 0 0 6.6 6.6l2.2-2.2a1 1 0 0 1 1-.25 11 11 0 0 0 3.6.6 1 1 0 0 1 1 1V20a1 1 0 0 1-1 1A17 17 0 0 1 3 4a1 1 0 0 1 1-1h3.5a1 1 0 0 1 1 1c0 1.25.2 2.45.6 3.6a1 1 0 0 1-.25 1z"/></svg></p>
      <p class="contact__row" style="margin-top:12px"><span>www.<span class="hl">heliosproperty</span>.com</span>
        <svg class="icon" viewBox="0 0 24 24"><path d="M2 5h20v14H2z"/><path d="M3 6.5l9 6.5 9-6.5" fill="none" stroke="#fff" stroke-width="1.6"/></svg></p>
      <p class="contact__row" style="margin-top:12px"><span>info@<span class="hl">heliosproperty</span>.com</span>
        <svg class="icon" viewBox="0 0 24 24"><circle cx="12" cy="12" r="10"/><path d="M2 12h20M12 2c3 3 3 17 0 20M12 2c-3 3-3 17 0 20M4 7h16M4 17h16" fill="none" stroke="#fff" stroke-width="1.4"/></svg></p>
    </div>
  </div>
</section>

<!-- BACK -->
<section class="postcard postcard--back" aria-label="Postcard back">
  <div class="postcard__inner">
    <svg class="postcard__shapes" viewBox="0 0 1157 723" aria-hidden="true">
      <rect width="1157" height="723" fill="var(--white)"/>
      <path d="M0,0 L545,0 C665,160 640,440 480,620 L0,620 Z" fill="var(--grey-band)"/>
      <path d="M0,0 L518,0 C625,160 600,430 455,620 L0,620 Z" fill="var(--blue)"/>
      <path d="M0,548 C120,522 270,522 480,552 L480,723 L0,723 Z" fill="var(--navy)"/>
      <path d="M0,572 C120,550 270,548 480,574 L480,723 L0,723 Z" fill="var(--white)"/>
      <path d="M548,680 L600,723 L584,723 Z" fill="var(--navy)"/>
      <circle cx="480" cy="590" r="115" fill="#f1f1f1"/>
    </svg>
    <div class="abs" role="img" aria-label="Photo of a happy family of three standing together in a bright home"
         style="left:375px;top:485px;width:210px;height:210px;border-radius:50%;background:radial-gradient(circle at 50% 40%,#e9e4dc,#a9b3bd)"></div>

    <p class="abs script" style="left:37px;top:28px">It’s simple.</p>
    <p class="abs intro" style="left:37px;top:86px">I am a new investor without down payment capital who still want to double our portfolio this year to grow our portfolio.</p>

    <div class="abs benefits">
      <div class="benefits__v"></div>
      <div class="benefits__h"></div>
      <p class="benefit" style="left:0;top:0"><svg class="icon" viewBox="0 0 24 24"><path d="M20 5a10 10 0 1 0 2 6h-2.2A8 8 0 1 1 18.3 6.6zM7 11l4 4 10-11 1.5 1.4L11 18 5.6 12.4z"/></svg><span>Formal protection<br>as a lien<br>holder against home</span></p>
      <p class="benefit" style="left:280px;top:0"><svg class="icon" viewBox="0 0 24 24"><path d="M20 5a10 10 0 1 0 2 6h-2.2A8 8 0 1 1 18.3 6.6zM7 11l4 4 10-11 1.5 1.4L11 18 5.6 12.4z"/></svg><span>No commission<br>or closing cost</span></p>
      <p class="benefit" style="left:0;top:75px"><svg class="icon" viewBox="0 0 24 24"><path d="M20 5a10 10 0 1 0 2 6h-2.2A8 8 0 1 1 18.3 6.6zM7 11l4 4 10-11 1.5 1.4L11 18 5.6 12.4z"/></svg><span>Fast closings<br>possible</span></p>
      <p class="benefit" style="left:280px;top:75px"><svg class="icon" viewBox="0 0 24 24"><path d="M20 5a10 10 0 1 0 2 6h-2.2A8 8 0 1 1 18.3 6.6zM7 11l4 4 10-11 1.5 1.4L11 18 5.6 12.4z"/></svg><span>Property taken as<br>is so no repairs</span></p>
    </div>

    <div class="abs option" style="left:37px;top:305px">
      <span class="option__label">OPTION 1</span>
      you can receive
      <span class="option__big"><span class="option__figure">80%</span>now cash</span>
      and <span class="option__inline">30%</span> over a short period of time including interest.
    </div>
    <div class="abs options__divider"></div>
    <div class="abs option" style="left:292px;top:305px">
      <span class="option__label">OPTION 2</span>
      we act like a bank, allowing you to make
      <span class="option__big"><span class="option__figure">150%</span></span>
      if you finance the whole property(ies).
    </div>
    <p class="abs option-tagline" style="left:37px;top:486px">No gimmicks and surprises, just simple unconventional financing.</p>

    <div class="abs contact contact--back" style="top:588px">
      <p class="contact__title" style="font-size:20px">CONTACT INFORMATION</p>
      <p class="contact__row contact__phone" style="margin-top:14px">
        <svg class="icon" viewBox="0 0 24 24"><path d="M6.6 10.8a15 15 0 0 0 6.6 6.6l2.2-2.2a1 1 0 0 1 1-.25 11 11 0 0 0 3.6.6 1 1 0 0 1 1 1V20a1 1 0 0 1-1 1A17 17 0 0 1 3 4a1 1 0 0 1 1-1h3.5a1 1 0 0 1 1 1c0 1.25.2 2.45.6 3.6a1 1 0 0 1-.25 1z"/></svg><span>5550142876</span></p>
      <p class="contact__row" style="margin-top:9px">
        <svg class="icon" viewBox="0 0 24 24"><path d="M2 5h20v14H2z"/><path d="M3 6.5l9 6.5 9-6.5" fill="none" stroke="#fff" stroke-width="1.6"/></svg><span>info@<span class="hl">heliosproperty</span>.com</span></p>
      <p class="contact__row" style="margin-top:9px">
        <svg class="icon" viewBox="0 0 24 24"><circle cx="12" cy="12" r="10"/><path d="M2 12h20M12 2c3 3 3 17 0 20M12 2c-3 3-3 17 0 20M4 7h16M4 17h16" fill="none" stroke="#fff" stroke-width="1.4"/></svg><span>www.heliosproperty.com</span></p>
    </div>

    <div class="abs brand" style="left:690px;top:70px">
      <div class="brand__mark" style="width:78px;height:78px"></div>
      <div class="brand__name"><span class="l1" style="font-size:42px">HELIOS</span><span class="l2" style="font-size:16px">PROPERTY GROUP</span></div>
    </div>
    <div class="abs stamp" style="left:977px;top:35px"></div>
    <div class="abs address-line" style="left:690px;top:342px"></div>
    <div class="abs address-line" style="left:690px;top:430px"></div>
    <div class="abs address-line" style="left:690px;top:518px"></div>
  </div>
</section>

</body>
</html>
```